Tirovel

We need a business card for our company is a holding for different business all are different we try to have some air of relax and fun in our projects we add pictures of the office to give you an idea od the mood of the business

Business

```html
<!DOCTYPE html>
<html lang="en">
<head>
<meta charset="utf-8">
<title>Tirovel Business Card</title>
<link rel="stylesheet" href="https://fonts.googleapis.com/css2?family=Archivo:wght@700&family=Oswald:wght@300;400&display=swap">
<style>
  :root {
    --charcoal: #3b393a;
    --banana: #f4ea3b;
    --white: #ffffff;
  }
  * { margin: 0; padding: 0; box-sizing: border-box; }
  html, body {
    width: 1200px;
    height: 720px;
    overflow: hidden;
    background: var(--charcoal);
  }
  .card {
    position: relative;
    width: 1200px;
    height: 720px;
    background: var(--charcoal);
    overflow: hidden;
    font-family: "Oswald", "Arial Narrow", sans-serif;
    font-weight: 300;
    color: var(--white);
  }
  .crescent {
    position: absolute;
    inset: 0;
    width: 1200px;
    height: 720px;
  }
  .brand-name {
    position: absolute;
    left: 50px;
    top: 34px;
    font-family: "Archivo", "Helvetica Neue", Arial, sans-serif;
    font-weight: 700;
    font-size: 128px;
    line-height: 0.82;
    letter-spacing: -7px;
    color: var(--white);
  }
  .brand-name span { display: block; }
  .identity {
    position: absolute;
    right: 34px;
    top: 30px;
    text-align: right;
    line-height: 1.15;
  }
  .identity .person-name {
    font-weight: 400;
    font-size: 38px;
  }
  .identity .role {
    font-size: 25px;
  }
  .contact-list {
    position: absolute;
    left: 714px;
    top: 500px;
    list-style: none;
    font-size: 28px;
  }
  .contact-list li { height: 51px; }
  .website {
    position: absolute;
    left: 43px;
    top: 602px;
    font-size: 28px;
  }
  .business-band {
    position: absolute;
    left: 0;
    bottom: 0;
    width: 1200px;
    height: 50px;
    background: var(--banana);
    display: flex;
    align-items: center;
    padding-left: 132px;
    color: var(--charcoal);
    font-size: 28px;
    list-style: none;
  }
  .business-band li {
    display: flex;
    align-items: center;
  }
  .business-band li + li::before {
    content: "";
    display: inline-block;
    width: 5px;
    height: 34px;
    background: var(--charcoal);
    margin: 0 28px 0 29px;
  }
</style>
</head>
<body>
  <div class="card">
    <svg class="crescent" viewBox="0 0 1200 720" aria-hidden="true">
      <circle cx="69" cy="-137" r="643" fill="none" stroke="var(--banana)" stroke-width="131"/>
    </svg>

    <h1 class="brand-name"><span>Tiro</span><span>vel</span></h1>

    <div class="identity">
      <p class="person-name">Your Name</p>
      <p class="role">Designation</p>
    </div>

    <ul class="contact-list">
      <li>Office Address :</li>
      <li>Contact No. :</li>
      <li>e-mail :</li>
    </ul>

    <p class="website">Visit us at : www.tirovel.com</p>

    <ul class="business-band">
      <li>business name</li>
      <li>business name</li>
      <li>business name</li>
      <li>business name</li>
      <li>business name</li>
    </ul>
  </div>
</body>
</html>
```